Business Card Design for Occupational Medicine Start Up Company

We need to design a professional business card. We are a healthcare company providing occupational medicine services to blue collar industries. We are professional, efficient and high quality service providers.

Target Market(s)

Blue Collar Industry: Shipbuilding, Ports, Trucking Companies; The Executives and Safety Officers for these companies

Industry/Entity Type

Healthcare

Contact Information for Business Card

Logo, Name, Title, Email, Phone

Other font styles liked:
• Please match our Brand Guide

Requirements
Must have
• Our Company Colors and Logo

```html
<!DOCTYPE html>
<html lang="en">
<head>
<meta charset="utf-8">
<title>CrewCare Clinics – Business Card</title>
<link href="https://fonts.googleapis.com/css2?family=Montserrat:wght@400;500;700&display=swap" rel="stylesheet">
<style>
  :root {
    --backdrop: #979797;
    --paper: #ffffff;
    --brand-indigo: #2b3480;
    --brand-sky: #24a8e0;
    --brand-gold: #f3b152;
    --deep-navy: #02134a;
    --royal-navy: #05258a;
    --ink-light: #ffffff;
  }
  * { margin: 0; padding: 0; box-sizing: border-box; }
  html, body { width: 1200px; height: 1200px; overflow: hidden; }
  body {
    background: var(--backdrop);
    position: relative;
    font-family: "Montserrat", sans-serif;
  }
  .card {
    position: absolute;
    left: 168px;
    width: 864px;
    height: 494px;
    background: var(--paper);
    overflow: hidden;
  }
  .card--front { top: 89px; }
  .card--back { top: 617px; background: var(--deep-navy); }
  .card svg.waves, .card svg.arcs {
    position: absolute; inset: 0; width: 100%; height: 100%;
  }
  .brand {
    position: absolute;
    text-align: center;
    color: var(--brand-indigo);
    font-weight: 700;
    transform: translateX(-50%);
    white-space: nowrap;
  }
  .brand__dot {
    display: block;
    margin: 0 auto;
    border-radius: 50%;
    background: var(--brand-indigo);
  }
  .brand__name { display: block; line-height: 1; }
  .brand__sub { display: block; line-height: 1; }
  .card--front .brand { left: 432px; top: 120px; }
  .card--front .brand__dot { width: 80px; height: 80px; margin-bottom: 30px; }
  .card--front .brand__name { font-size: 46px; letter-spacing: 1px; }
  .card--front .brand__sub { font-size: 25px; letter-spacing: 12px; margin-top: 10px; padding-left: 12px; }
  .card--back .brand { left: 198px; top: 165px; }
  .card--back .brand__dot { width: 56px; height: 56px; margin-bottom: 22px; }
  .card--back .brand__name { font-size: 30px; letter-spacing: 1px; }
  .card--back .brand__sub { font-size: 17px; letter-spacing: 8px; margin-top: 7px; padding-left: 8px; }
  .contact {
    position: absolute;
    left: 493px;
    top: 102px;
    color: var(--ink-light);
  }
  .contact__name {
    font-size: 50px;
    font-weight: 700;
    color: var(--brand-sky);
    line-height: 1;
  }
  .contact__email { font-size: 20px; margin-top: 4px; }
  .contact__address { font-size: 20.5px; line-height: 25px; margin-top: 44px; }
  .contact__phones { font-size: 20.5px; line-height: 25px; margin-top: 24px; }
  .contact__web { font-size: 20.5px; margin-top: 24px; }
</style>
</head>
<body>

<section class="card card--front">
  <svg class="waves" viewBox="0 0 1391 795" preserveAspectRatio="none" aria-hidden="true">
    <defs>
      <linearGradient id="navyFade" x1="0" y1="0" x2="0" y2="1">
        <stop offset="0.62" stop-color="var(--royal-navy)"/>
        <stop offset="0.85" stop-color="var(--deep-navy)"/>
      </linearGradient>
      <filter id="softShadow" x="-5%" y="-20%" width="110%" height="140%">
        <feDropShadow dx="0" dy="-3" stdDeviation="4" flood-color="#000" flood-opacity="0.35"/>
      </filter>
    </defs>
    <path fill="var(--brand-sky)" d="M0,601 C200,575 450,585 600,620 S850,670 1000,655 C1100,645 1200,600 1300,566 L1391,560 V795 H0Z"/>
    <path fill="var(--brand-gold)" filter="url(#softShadow)" d="M0,666 C200,640 450,640 600,670 S850,700 950,688 C1100,670 1200,600 1300,545 C1340,536 1370,540 1391,546 V795 H0Z"/>
    <path fill="url(#navyFade)" filter="url(#softShadow)" d="M0,672 C200,652 450,652 600,686 S850,726 950,716 C1100,700 1200,640 1280,605 C1330,590 1370,600 1391,611 V795 H0Z"/>
  </svg>
  <div class="brand">
    <span class="brand__dot"></span>
    <span class="brand__name">CREWCARE</span>
    <span class="brand__sub">CLINICS</span>
  </div>
</section>

<section class="card card--back">
  <svg class="arcs" viewBox="0 0 1391 795" preserveAspectRatio="none" aria-hidden="true">
    <defs>
      <filter id="edgeShadow" x="-10%" y="-10%" width="130%" height="120%">
        <feDropShadow dx="5" dy="0" stdDeviation="6" flood-color="#000" flood-opacity="0.45"/>
      </filter>
    </defs>
    <path fill="var(--brand-indigo)" d="M0,0 H484 C742,200 742,560 534,795 H0Z"/>
    <path fill="var(--brand-gold)" filter="url(#edgeShadow)" d="M0,0 H470 C723,200 723,560 504,795 H0Z"/>
    <path fill="var(--brand-sky)" filter="url(#edgeShadow)" d="M0,0 H455 C703,200 703,560 480,795 H0Z"/>
    <path fill="var(--paper)" filter="url(#edgeShadow)" d="M0,0 H444 C678,200 678,560 439,795 H0Z"/>
  </svg>
  <div class="brand">
    <span class="brand__dot"></span>
    <span class="brand__name">CREWCARE</span>
    <span class="brand__sub">CLINICS</span>
  </div>
  <div class="contact">
    <h1 class="contact__name">Full Name</h1>
    <p class="contact__email">full.name@crewcareclinics.com</p>
    <p class="contact__address">123 Main Road, Suite 345<br>East North, State 12345</p>
    <p class="contact__phones">T: 123-456-7890<br>F: 123-456-7890</p>
    <p class="contact__web">crewcareclinics.com</p>
  </div>
</section>

</body>
</html>
```